Für das neue Tantra-Bildungszetrum: 8-oder 10-Seiten-Faltblatt und ein Plakat DIN A3
Zielgruppe
Es geht darum, über das Angebot des neuen Bildungszentrums Kreis der Morgenröte zu informieren.
Das Zentrum organisiert und führt regelmäßige Veranstaltungen wie Info-Vorträge, Schnuppertage, Seminare, Kurse und Intensivtrainings durch, ist in allem spezialisiert auf Tantra. Das Zentrum ist vertreten an mehreren Standorten Deutschlands durch das jeweils ein Team an Lehrern und Dozenten. Für die Veranstaltungen werden externe Räume angemietet. Das Angebot soll in jeder Stadt, wo die Broschüren oder Faltblätter verteilt werden. Die Anmeldung und Registrierung erfolgt über die neue Homepage, die bald freigegeben wird und noch nicht zur Verfügung steht.
Das Besondere am Zentrum ist die Möglichkeit, eigene tantrische Selbsterfahrungen zu machen und entweder später oder als Option sich gleich für einen der sechs neuen Tantra- Ausbildungsberufe zu entscheiden.
Darüber hinaus, soll die Broschüre oder die Faltblätter zur Mitarbeit und Kooperation mit selbständigen Yoga- und Tantra-Lehrern, sowie Ärzten, Therapeuten und Heilpraktiken einladen.
Das Bildungszentrum ist ein Netzwerk der Honorar-Dozenten, die entweder Lehrer und Experte auf dem tantrischen Bereich oder Vertreter der klassischen und alternativen Heilkunde oder beides zusammen sind.
Wer ist die Zielgruppe? Männer und Frauen, vom 18 - 60 Jahre. Menschen, die sich für Tantra und Selbsterfahrung interessieren, und Menschen, die nach einer neuen beruflichen Perspektive suchen.
Aufgabenstellung
1). 10-Seiten- Faltblatt designen
2). Plakat DIN A3 gestalten

```html
<!DOCTYPE html>
<html lang="de">
<head>
<meta charset="utf-8">
<title>Bildungszentrum Kreis der Morgenröte – Plakat</title>
<link rel="stylesheet" href="https://fonts.googleapis.com/css2?family=Roboto+Slab:wght@400;700&family=Ubuntu:wght@400;500;700&display=swap">
<style>
  :root {
    --teal: #2c7c72;
    --teal-light: #6aa59d;
    --teal-text: #2f8377;
    --orange: #e9742a;
    --orange-soft: #f2913f;
    --white: #ffffff;
    --photo-a: #c85a2c;
    --photo-b: #f2a468;
    --portrait-a: #6b4a3a;
    --portrait-b: #b8a08a;
  }
  * { box-sizing: border-box; margin: 0; padding: 0; }
  html, body { width: 849px; height: 1200px; overflow: hidden; background: var(--white); }
  .poster {
    position: relative; width: 849px; height: 1200px; overflow: hidden;
    background: var(--teal); font-family: "Roboto Slab", serif; color: var(--white);
  }
  .header-wave { position: absolute; left: 0; top: 0; width: 849px; height: 300px; }

  .brand-dot { position: absolute; left: 160px; top: 68px; width: 90px; height: 90px; border-radius: 50%; background: var(--orange); }
  .brand-name { position: absolute; left: 270px; top: 72px; font-family: "Ubuntu", sans-serif; color: var(--teal-text); line-height: 1.1; }
  .brand-name .line-small { display: block; font-size: 34px; font-weight: 400; }
  .brand-name .line-large { display: block; font-size: 44px; font-weight: 700; }

  .intro {
    position: absolute; left: 33px; top: 292px; width: 562px;
    font-size: 15px; line-height: 21px; text-align: justify; hyphens: auto;
  }
  .drop-cap { float: left; font-size: 48px; line-height: 38px; color: var(--orange); margin: 4px 3px 0 0; }

  .hero-photo {
    position: absolute; left: 603px; top: 248px; width: 254px; height: 254px; border-radius: 50%;
    background: radial-gradient(circle at 40% 40%, var(--photo-b), var(--photo-a));
    box-shadow: 0 0 0 9px var(--orange);
  }

  .offer { position: absolute; font-size: 13px; line-height: 18.5px; hyphens: auto; }
  .offer-head { font-weight: 700; }
  .accent { color: var(--orange-soft); }
  .offer-list { list-style: none; font-weight: 400; }

  .mandala {
    position: absolute; width: 76px; height: 76px; border-radius: 50%;
    background: radial-gradient(circle, var(--orange-soft) 0 22%, transparent 23% 40%, var(--orange) 41% 48%, transparent 49%);
  }
  .divider { position: absolute; top: 738px; height: 1px; background: rgba(255,255,255,0.7); }

  .contact-band { position: absolute; left: 0; top: 1012px; width: 849px; height: 188px; background: var(--teal-light); }
  .contact-title { position: absolute; left: 222px; top: 1014px; font-family: "Ubuntu", sans-serif; font-size: 22px; font-weight: 700; color: var(--orange-soft); }
  .portrait {
    position: absolute; left: 15px; top: 1032px; width: 135px; height: 135px; border-radius: 50%;
    background: radial-gradient(circle at 50% 40%, var(--portrait-b), var(--portrait-a));
  }
  .contact-list { position: absolute; left: 190px; top: 1050px; list-style: none; font-size: 17px; font-weight: 500; font-family: "Ubuntu", sans-serif; }
  .contact-list li { display: flex; align-items: center; gap: 12px; height: 31px; }
  .contact-icon { width: 20px; height: 20px; flex: none; }
</style>
</head>
<body>
<main class="poster">
  <svg class="header-wave" viewBox="0 0 849 300" aria-hidden="true">
    <path d="M0 0 H849 V262 C720 238 600 222 470 232 C320 244 160 262 0 250 Z" fill="var(--orange)"/>
    <path d="M0 0 H849 V240 C720 222 600 210 470 218 C320 228 160 246 0 236 Z" fill="var(--white)"/>
  </svg>

  <span class="brand-dot"></span>
  <div class="brand-name"><span class="line-small">Bildungszentrum</span><span class="line-large">Kreis der Morgenröte</span></div>

  <div class="hero-photo" role="img" aria-label="Foto eines Paares in inniger Umarmung in warmem Licht"></div>

  <p class="intro"><span class="drop-cap">U</span>nser Bildungszentrum soll viele Menschen bei ihren inneren Transformationsprozessen unterstützen indem es spezielle berufliche Perspektiven anbietet, bei denen Selbstverwirklichung in authentischem Kontakt mit anderen Menschen möglich ist. Wenn die innere Welt in Frieden, Harmonie und Ruhe ist, so wird sich dies auch auf unsere äußere Welt auswirken und initiiert so einen Gesellschaftwandel durch innere Transformation. Tantra liefert uns Techniken, die unser Bewusstsein durch die Transformation innerer Vorgänge grundlegend wandeln. Tantra unterstützt Menschen in ihrem Bemühen um spirituelles Wachstum, Selbstverwirklichung, innere Entwicklung sowie der Verbesserung ihrer Liebes- und Lustfähigkeit. Es fördert das Aufblühen der eigenen inneren Göttlichkeit und das Nutzen von sexueller Energie im spirituellen Sinne. Dies ist nur kleiner Ausschnitt dessen, was Tantra uns ermöglicht.</p>

  <div class="mandala" style="left:27px; top:630px" role="img" aria-label="Orangefarbenes Mandala-Ornament"></div>
  <div class="offer" style="left:132px; top:632px; width:285px">
    <p class="offer-head">Wir laden dich herzlich zu unseren <span class="accent">regelmäßigen Vorträgen</span> ein:</p>
    <ol class="offer-list"><li>1. Was ist Tantra?</li><li>2. Berufliche Perspektiven mit Tantra.</li></ol>
  </div>
  <div class="divider" style="left:132px; width:265px"></div>

  <div class="mandala" style="left:27px; top:772px" role="img" aria-label="Orangefarbenes Mandala-Ornament"></div>
  <div class="offer" style="left:132px; top:762px; width:285px">
    <p class="offer-head">Steige ein in den nächsten<br><span class="accent">12- Wochen Tantra-Kurs:</span></p>
    <ul class="offer-list" style="margin-top:24px">
      <li>•&nbsp;&nbsp;”Tantra für Anfänger”</li>
      <li>•&nbsp;&nbsp;”Tantra für Mittelstufe”</li>
      <li>•&nbsp;&nbsp;”Tantra für Fortgeschrittene”</li>
    </ul>
  </div>

  <div class="mandala" style="left:428px; top:645px" role="img" aria-label="Orangefarbenes Mandala-Ornament"></div>
  <div class="offer" style="left:532px; top:632px; width:280px; text-align:justify">
    <p class="offer-head">Erfahre den Geschmack, den Geruch, die Farbe und den Klang von Tantra bei einem unserer <span class="accent">Schnuppertage oder Einsteiger-Wochenenden.</span></p>
  </div>
  <div class="divider" style="left:532px; width:278px"></div>

  <div class="mandala" style="left:428px; top:772px" role="img" aria-label="Orangefarbenes Mandala-Ornament"></div>
  <div class="offer" style="left:532px; top:756px; width:280px; text-align:justify">
    <p class="offer-head">Mach Tantra zu deinem Beruf! Investiere zwei bis fünf wundervolle Jahre je nach deiner Wahl in eine <span class="accent">Berufsausbildung mit Zukunft!</span> Welche unserer sechs Ausbildungsberufe spricht dich an?</p>
  </div>
  <ol class="offer offer-list" style="left:532px; top:893px; width:280px">
    <li>1. Tantra-Lehrer</li>
    <li>2. Tantra-Yoga-Lehrer</li>
    <li>3. Tantrischer Massagetherapeut</li>
    <li>4. Tantrischer Sexualtherapeut</li>
    <li>5. Tantra-Coach</li>
    <li>6. Selbst Ausbilder werden</li>
  </ol>

  <div class="contact-band"></div>
  <div class="portrait" role="img" aria-label="Porträtfoto der Ansprechpartnerin"></div>
  <div class="contact-title">Kontakt:</div>
  <ul class="contact-list">
    <li>
      <svg class="contact-icon" viewBox="0 0 20 20" aria-hidden="true"><circle cx="10" cy="10" r="8.5" fill="none" stroke="#fff" stroke-width="1.6"/><ellipse cx="10" cy="10" rx="3.6" ry="8.5" fill="none" stroke="#fff" stroke-width="1.4"/><path d="M1.5 10 H18.5" stroke="#fff" stroke-width="1.4"/></svg>
      www.morgenroete-kreis.de
    </li>
    <li>
      <svg class="contact-icon" viewBox="0 0 20 20" aria-hidden="true"><path d="M5 2 L8 6 L6.5 8 C7.5 10.5 9.5 12.5 12 13.5 L14 12 L18 15 L16 18 C9 18 2 11 2 4 Z" fill="#fff"/></svg>
      0176 52 31 87 40
    </li>
    <li>
      <svg class="contact-icon" viewBox="0 0 20 20" aria-hidden="true"><rect x="2" y="2" width="16" height="16" fill="#fff"/></svg>
      Tantra.Bildungszentrum.KreisDerMorgenroete
    </li>
    <li>
      <svg class="contact-icon" viewBox="0 0 20 20" aria-hidden="true"><rect x="2" y="2" width="16" height="16" fill="#fff"/></svg>
      KreisDerMorgenroete
    </li>
  </ul>
</main>
</body>
</html>
```